依頼概要
■依頼の目的/概要
弊社の経営理念を作成しましたが、社内掲示用にポスターの作成をお願いします。

■依頼詳細
ミッション・ビジョン・バリューをポスター1枚に収めてください。
HPにも掲載できればと考えています。

■重視する点
掲載内容は添付ファイルをご確認ください。

過去の提案(同業者なので)を見て応募しようと考えました。
https://www.pitchora.jp/work/detail/4731852

■弊社の紹介
東京都内で廃棄物を収集・処分する会社です。詳しくは下記Official HPをご覧ください。
https://www.miyakura-k.co.jp

HP検討挿入予定個所
https://www.miyakura-k.co.jp/company

■その他
掲載内容の文言はあまり整理されていないのでうまい具合にご調整ください。

■その他ご不明点はお気軽にお問合せください。

発注時のイメージ通りの作品だったため。

この度は、沢山のご応募ありがとうございます。
皆さんのご提案が多く、選定に迷いました。

また機会がございましたら、よろしくお願いします。

```html
<!DOCTYPE html>
<html lang="ja">
<head>
<meta charset="utf-8">
<title>MIYAKURA 経営理念ポスター</title>
<link rel="stylesheet" href="https://fonts.googleapis.com/css2?family=Libre+Baskerville&family=Noto+Serif+JP:wght@500;700&family=Noto+Sans+JP:wght@500;700&display=swap">
<style>
  :root{
    --sky-top:#7fb6e6;
    --sky-mid:#bcdaf3;
    --sky-low:#f3f8fc;
    --navy:#1c4c7d;
    --accent:#d98a2b;
    --ink:#23303d;
    --brand:#1d7f8f;
    --leaf-light:#b9dc6a;
    --leaf-mid:#7fbf3e;
    --leaf-deep:#4f9a2c;
  }
  *{margin:0;padding:0;box-sizing:border-box}
  html,body{width:851px;height:1200px;overflow:hidden;background:#fff}
  .poster{
    position:relative;width:851px;height:1200px;overflow:hidden;
    background:linear-gradient(180deg,var(--sky-top) 0%,var(--sky-mid) 28%,var(--sky-low) 58%,#ffffff 75%);
    font-family:"Noto Serif JP",serif;color:var(--ink);
  }
  .sky{
    position:absolute;inset:0 0 auto 0;height:900px;
    background:
      radial-gradient(ellipse 320px 110px at 120px 400px,rgba(255,255,255,.85),transparent 70%),
      radial-gradient(ellipse 360px 120px at 720px 340px,rgba(255,255,255,.8),transparent 70%),
      radial-gradient(ellipse 300px 90px at 430px 640px,rgba(255,255,255,.7),transparent 70%);
  }
  .brand{position:absolute;left:28px;top:26px;display:flex;align-items:center;gap:10px;z-index:2}
  .brand-dot{width:34px;height:34px;border-radius:50%;background:var(--brand)}
  .brand-name{font-family:"Noto Sans JP",sans-serif;font-weight:700;font-size:30px;letter-spacing:1px;color:var(--brand);line-height:1}
  .brand-sub{font-family:"Noto Sans JP",sans-serif;font-weight:700;font-size:11px;color:var(--brand);letter-spacing:3px;margin-top:4px}
  .statement{position:absolute;left:0;width:100%;text-align:center;z-index:2}
  .statement h2{font-family:"Libre Baskerville",serif;font-weight:400;font-size:64px;color:var(--navy);line-height:1;letter-spacing:1px}
  .statement .label{display:inline-block;margin-top:8px;font-weight:700;font-size:26px;line-height:1.3;color:var(--accent);letter-spacing:2px;padding:0 24px 6px;border-bottom:2px solid var(--accent)}
  .statement p{margin-top:14px;font-weight:700;font-size:19px;line-height:1.75;letter-spacing:.5px}
  .mission{top:140px}
  .vision{top:405px}
  .value{top:670px}
  .trees{
    position:absolute;left:0;bottom:0;width:100%;height:240px;z-index:1;
    border-radius:48% 52% 0 0 / 30% 28% 0 0;
    background:linear-gradient(180deg,var(--leaf-light) 0%,var(--leaf-mid) 45%,var(--leaf-deep) 100%);
  }
</style>
</head>
<body>
<main class="poster">
  <div class="sky" role="img" aria-label="雲が浮かぶ明るい青空"></div>

  <header class="brand">
    <span class="brand-dot"></span>
    <div>
      <div class="brand-name">MIYAKURA</div>
      <div class="brand-sub">株式会社宮倉興業</div>
    </div>
  </header>

  <section class="statement mission">
    <h2>Mission</h2>
    <div class="label">社会的使命</div>
    <p>地球環境を保全するために、<br>静脈産業を支える社会インフラの一部としての役割を全うし、<br>すべての人に快適でクリーンな世界を提供する</p>
  </section>

  <section class="statement vision">
    <h2>Vision</h2>
    <div class="label">中長期計画</div>
    <p>先進的(Advanced)な取り組みを行い廃棄物業界リード(Lead)し<br>高品質(High quality)なサービスを提供し<br>働きがいのある(Satisfaction)会社づくりを行う</p>
  </section>

  <section class="statement value">
    <h2>Value</h2>
    <div class="label">大切な価値観</div>
    <p>活発なコミュニケーションの元、情報共有を行い、<br>チームワーク溢れる組織風土の中で、共働し、<br>何事にも真摯に向き合い、正直な気持ちで、<br>チャレンジ行動力をもって、自己実現を目指す</p>
  </section>

  <div class="trees" role="img" aria-label="若葉色の木々が並ぶ森のイラスト"></div>
</main>
</body>
</html>
```